business card for author of crime novel

I am an author with a new book. I need a business card with the book's cover on one side (already uploaded), and contact details on the other.

Walt Pemberty
Author

telephone: 646-512-7380
website: www.waltpemberty.net
facebook: friendline.net/wpemberty
twitter: chirpwire.net/wpemberty
email: wpemberty@postvale.net

Target Market(s)

Readers of mystery books

Industry/Entity Type

Business

Contact Information for Business Card

Walt Pemberty
Author

telephone: 646-512-7380

Font styles to use
Serif
Sans Serif

Requirements
Must have
• Book cover on one side. My contact info on the other, with the name of the book repeated if that makes sense. Clean design.
Should not have
• Overly ornate, too formal, too distracting

```html
<!DOCTYPE html>
<html lang="en">
<head>
<meta charset="utf-8">
<title>Night Desk Noir – Business Card</title>
<link href="https://fonts.googleapis.com/css2?family=Cinzel:wght@700&family=IM+Fell+English&family=Oswald:wght@400&display=swap" rel="stylesheet">
<style>
  :root {
    --canvas-bg: #f2f2f4;
    --card-gold: #cc9429;
    --ink: #111111;
    --cover-dark: #1f2c36;
    --cover-mid: #5f7a8a;
    --cover-light: #a9bcc6;
    --cover-name: #f4e51c;
    --banner-paper: #e2c88f;
    --banner-edge: #b89a5e;
    --banner-ink: #2a2118;
  }
  * { margin: 0; padding: 0; box-sizing: border-box; }
  html, body { width: 1200px; height: 1000px; overflow: hidden; }
  body { background: var(--canvas-bg); position: relative; }

  .card {
    position: absolute;
    top: 163px;
    width: 385px;
    height: 673px;
    background: var(--card-gold);
    color: var(--ink);
  }
  .card--front { left: 164px; }
  .card--back { left: 650px; }

  .book-title {
    position: absolute;
    top: 72px;
    left: 0; right: 0;
    text-align: center;
    font-family: "Cinzel", serif;
    font-weight: 700;
    font-size: 28px;
    letter-spacing: 1px;
    white-space: nowrap;
  }

  .cover-art {
    position: absolute;
    left: 40px;
    top: 130px;
    width: 306px;
    height: 407px;
    background: linear-gradient(160deg, var(--cover-light) 0%, var(--cover-mid) 35%, var(--cover-dark) 100%);
  }
  .cover-author {
    position: absolute;
    right: 8px;
    bottom: 10px;
    width: 160px;
    text-align: center;
    font-family: "Cinzel", serif;
    font-weight: 700;
    font-size: 19px;
    line-height: 22px;
    color: var(--cover-name);
  }

  .series-banner {
    position: absolute;
    left: 39px;
    top: 551px;
    width: 308px;
    height: 54px;
    background: var(--banner-paper);
    border-radius: 6px;
    border-left: 4px solid var(--banner-edge);
    box-shadow: 0 3px 4px rgba(0,0,0,0.25);
    display: flex;
    align-items: center;
    justify-content: center;
    font-family: "Oswald", sans-serif;
    font-size: 22px;
    color: var(--banner-ink);
  }

  .contact-name,
  .contact-role,
  .contact-list,
  .contact-web {
    position: absolute;
    left: 0; right: 0;
    text-align: center;
    font-family: "IM Fell English", serif;
    white-space: nowrap;
  }
  .contact-name { top: 234px; font-size: 29px; }
  .contact-role { top: 274px; font-size: 24px; }
  .contact-list {
    top: 330px;
    list-style: none;
    font-size: 19px;
    line-height: 27px;
  }
  .contact-web { top: 574px; font-size: 18px; letter-spacing: 0.3px; }
</style>
</head>
<body>
  <section class="card card--front">
    <h1 class="book-title">NIGHT DESK NOIR</h1>
    <div class="cover-art" role="img" aria-label="Book cover photograph of an old brick tenement building with fire escapes, in cold blue tones">
      <div class="cover-author">WALT<br>PEMBERTY</div>
    </div>
    <div class="series-banner">A Harlan Voss Mystery</div>
  </section>

  <section class="card card--back">
    <h2 class="book-title">NIGHT DESK NOIR</h2>
    <p class="contact-name">Walt Pemberty</p>
    <p class="contact-role">Author</p>
    <ul class="contact-list">
      <li>Telephone : 646-512-7380</li>
      <li>Email : wpemberty@postvale.net</li>
      <li>Friendline : friendline.net/wpemberty</li>
      <li>Chirpwire : chirpwire.net/wpemberty</li>
    </ul>
    <p class="contact-web">www.waltpemberty.net</p>
  </section>
</body>
</html>
```